Tallow Accounting Business Card design

We need a stand out business card design for Accounting practice based in Australia specialising in pubs, clubs and hotels. We help venues maximise margins, create time and manage cashflow. One club we have been working with for the last 6 months has increased revenue by 3% and margin by 5% in this time frame. We have a back office outsourced system that costs less than having a full time employee and also allows the venues the added benefit of:<br/>-using the office space to become a revenue generating opportunity. <br/>-a complete system to enhance governance, accountability and efficiency within their operation<br/>-52 weeks cover so no hassle to cover annual/sick .. leave<br/><br/>We would like to see designs that use the colours of our logo (green & blue).
Target Market(s)
Australian Pubs, Clubs & Hotels abookkeeping, accounting and tax services
Industry/Entity Type
Accountant
Contact Information for Business Card
Miriel Dawkes CPA
Principal
Accountant Tax Agent
Miriel@TallowAccounting.example.au
0418639174
www.tallowaccounting.example.au
Accounting / Payroll / Tax / SMSF / Technology
Colors
Designer to choose colors to be used in the design.
Look and feel
Each slider illustrates characteristics of the customer's brand and the style your logo design should communicate.

```html
<!DOCTYPE html>
<html lang="en">
<head>
<meta charset="utf-8">
<title>Tallow Accounting – Business Card</title>
<link rel="stylesheet" href="https://fonts.googleapis.com/css2?family=Archivo:wght@700&family=Mulish:wght@400;700&display=swap">
<style>
  :root {
    --brand-blue: #233f90;
    --brand-green: #0a7040;
    --paper: #ffffff;
    --backdrop: #ece8e1;
    --text-grey: #555a60;
    --badge-dark: #111111;
    --badge-grey: #9a9a9a;
  }
  * { margin: 0; padding: 0; box-sizing: border-box; }
  html, body { width: 1200px; height: 900px; overflow: hidden; }
  body {
    position: relative;
    background: var(--backdrop);
    font-family: "Mulish", "Helvetica Neue", Arial, sans-serif;
  }
  .card {
    position: absolute;
    left: 311px;
    width: 577px;
    height: 329px;
    box-shadow: 0 4px 10px rgba(0,0,0,0.18);
    overflow: hidden;
  }
  /* Front */
  .card-front { top: 98px; background: var(--brand-blue); }
  .front-wordmark {
    position: absolute;
    left: 148px;
    top: 118px;
    display: flex;
    align-items: center;
    gap: 18px;
    color: var(--paper);
    font-family: "Archivo", "Arial Black", sans-serif;
    font-weight: 700;
  }
  .wordmark-dot {
    width: 70px; height: 70px;
    border: 3px solid var(--paper);
    border-radius: 50%;
    flex: none;
  }
  .wordmark-text { display: flex; flex-direction: column; line-height: 1; }
  .wordmark-name { font-size: 54px; letter-spacing: -1px; }
  .wordmark-sub { font-size: 19px; letter-spacing: 1.5px; margin-top: 8px; text-transform: uppercase; }
  .services-band {
    position: absolute;
    left: 0; bottom: 0;
    width: 100%; height: 44px;
    background: var(--brand-green);
    color: var(--paper);
    font-size: 16px;
    display: flex; align-items: center; justify-content: center;
  }
  /* Back */
  .card-back { top: 472px; background: var(--paper); }
  .back-wordmark {
    position: absolute;
    left: 33px; top: 32px;
    display: flex; align-items: center; gap: 12px;
    color: var(--brand-blue);
    font-family: "Archivo", "Arial Black", sans-serif;
    font-weight: 700;
  }
  .back-wordmark .wordmark-dot { width: 52px; height: 52px; border-color: var(--brand-blue); }
  .back-wordmark .wordmark-name { font-size: 40px; }
  .back-wordmark .wordmark-sub { font-size: 15px; letter-spacing: 1.2px; margin-top: 5px; }
  .person {
    position: absolute;
    right: 33px; top: 135px;
    text-align: right;
    line-height: 17px;
    color: var(--brand-green);
    font-size: 14.5px;
  }
  .person-name { color: var(--brand-blue); font-size: 17px; font-weight: 700; line-height: 20px; }
  .person-name .credential { font-weight: 400; font-size: 15px; }
  .divider {
    position: absolute;
    left: 37px; right: 35px; top: 204px;
    height: 1.5px; background: var(--brand-blue);
  }
  .contact-list {
    position: absolute;
    left: 33px; top: 227px;
    list-style: none;
    color: var(--text-grey);
    font-size: 15px;
  }
  .contact-list li { display: flex; align-items: center; gap: 10px; height: 25.5px; }
  .contact-list svg { width: 16px; height: 16px; fill: var(--brand-blue); flex: none; }
  .memberships {
    position: absolute;
    right: 30px; top: 242px;
    display: flex; align-items: center; gap: 10px;
  }
  .badge-institute { width: 72px; height: 52px; background: var(--badge-grey); opacity: .5; }
  .badge-body { width: 77px; height: 34px; background: var(--badge-dark); }
  .badge-register { width: 40px; height: 40px; border-radius: 50%; background: var(--badge-grey); opacity: .6; }
</style>
</head>
<body>
  <section class="card card-front">
    <div class="front-wordmark">
      <span class="wordmark-dot"></span>
      <span class="wordmark-text">
        <span class="wordmark-name">Tallow</span>
        <span class="wordmark-sub">Accounting</span>
      </span>
    </div>
    <div class="services-band">Accounting | Payroll | Tax | SMSF | Technology</div>
  </section>

  <section class="card card-back">
    <div class="back-wordmark">
      <span class="wordmark-dot"></span>
      <span class="wordmark-text">
        <span class="wordmark-name">Tallow</span>
        <span class="wordmark-sub">Accounting</span>
      </span>
    </div>
    <div class="person">
      <div class="person-role">Principal</div>
      <div class="person-name">Miriel Dawkes <span class="credential">CPA</span></div>
      <div class="person-title">Accountant Tax Agent</div>
    </div>
    <div class="divider"></div>
    <ul class="contact-list">
      <li>
        <svg viewBox="0 0 24 24" aria-hidden="true"><path d="M6.6 10.8a15.1 15.1 0 0 0 6.6 6.6l2.2-2.2c.3-.3.7-.4 1-.2 1.1.4 2.3.6 3.6.6.6 0 1 .4 1 1V20c0 .6-.4 1-1 1A17 17 0 0 1 3 4c0-.6.4-1 1-1h3.5c.6 0 1 .4 1 1 0 1.3.2 2.5.6 3.6.1.3 0 .7-.2 1z"/></svg>
        041 863 9174
      </li>
      <li>
        <svg viewBox="0 0 24 24" aria-hidden="true"><path d="M2 5h20v2l-10 6L2 7z"/><path d="M2 9l10 6 10-6v10H2z"/></svg>
        miriel@tallowaccounting.example.au
      </li>
      <li>
        <svg viewBox="0 0 24 24" aria-hidden="true"><path d="M12 2a10 10 0 1 0 0 20 10 10 0 0 0 0-20zm-1 17.9A8 8 0 0 1 4.2 10L9 14.8v1a2 2 0 0 0 2 2zm6.9-2.5A2 2 0 0 0 16 16h-1v-3a1 1 0 0 0-1-1H8v-2h2a1 1 0 0 0 1-1V7h2a2 2 0 0 0 2-2v-.4a8 8 0 0 1 2.9 12.8z"/></svg>
        www.tallowaccounting.example.au
      </li>
    </ul>
    <div class="memberships">
      <span class="badge-institute" role="img" aria-label="Professional institute membership badge"></span>
      <span class="badge-body" role="img" aria-label="Accounting body membership badge"></span>
      <span class="badge-register" role="img" aria-label="Registered tax agent seal"></span>
    </div>
  </section>
</body>
</html>
```